Graphic picture for front page of website

We need a picture to place on the front page of our pressloft Website. The company name is Nova Grid , and we sell Tessary Sheets services. The website is www.novagridsheets.example . I am looking for something to go in the picture in the middle of the site, to replace the current default template. Currently we use the color green, as it is default, but happy for you to be creative to see what works (colorful is good). I have included just some random screenshots of projects I have done for clients, for some possible inspiration. Have a look at our services to see what kinds of work we do.
We currently have no logo, the lumora thing is just a default of the pressloft theme.
Updates
Hi guys, I have uploaded a picture to show you the dimensions (the ratio, please make the image large so it is very high quality, i can scale it to the exact size needed). All of the writing/key info should be in the red lines, people with smaller monitors will just see that, people with wide monitors will see all of it.
Thanks
No stock photos of people thanks.
Target Market(s)
Small to large business, looking for Tessary Sheets services.
Industry/Entity Type
It Company
Look and feel
Each slider illustrates characteristics of the customer's brand and the style your logo design should communicate.

```html
<!DOCTYPE html>
<html lang="en">
<head>
<meta charset="utf-8">
<title>Nova Grid – Tessary Sheets services banner</title>
<link rel="stylesheet" href="https://fonts.googleapis.com/css2?family=Roboto:wght@400;700&family=Roboto+Condensed:wght@400;700&display=swap">
<style>
  :root {
    --brand-red: #e31e24;
    --accent-orange: #f7a21b;
    --wood-dark: #2e2620;
    --wood-mid: #5a4a3c;
    --wood-light: #8a7664;
    --button-brown: #4a3426;
    --white: #ffffff;
    --device-light: #e9eaec;
    --device-mid: #c9ccd1;
  }
  * { margin: 0; padding: 0; box-sizing: border-box; }
  html, body { width: 1200px; height: 458px; overflow: hidden; background: var(--white); }
  .banner {
    position: relative;
    width: 1200px;
    height: 458px;
    overflow: hidden;
    font-family: "Roboto Condensed", Arial, sans-serif;
  }
  .banner__wood {
    position: absolute; inset: 0;
    background: radial-gradient(ellipse at 30% 20%, var(--wood-light) 0%, var(--wood-mid) 35%, var(--wood-dark) 80%);
  }
  .banner__red-field { position: absolute; inset: 0; }
  .headline {
    position: absolute;
    left: 25px; top: 54px;
    color: var(--accent-orange);
    font-family: "Roboto", Arial, sans-serif;
    font-size: 32px;
    font-weight: 400;
    letter-spacing: -0.5px;
    white-space: nowrap;
  }
  .headline strong { font-weight: 700; font-size: 36px; }
  .service {
    position: absolute;
    width: 124px; height: 124px;
    display: flex; align-items: center; justify-content: center;
  }
  .service::before {
    content: "";
    position: absolute; inset: 0;
    background: var(--brand-red);
    transform: rotate(45deg);
  }
  .service span {
    position: relative;
    color: var(--white);
    font-size: 24px;
    line-height: 1.25;
    text-align: center;
    white-space: nowrap;
  }
  .service--programming { left: 26px; top: 197px; }
  .service--finance { left: 181px; top: 163px; }
  .service--charts { left: 288px; top: 255px; }
  .service--analysis { left: 124px; top: 300px; }
  .more-note {
    position: absolute;
    left: 222px; top: 425px;
    color: var(--white);
    font-size: 21px;
  }
  .purchase-button {
    position: absolute;
    left: 467px; top: 332px;
    width: 158px; height: 158px;
    border-radius: 50%;
    background: var(--button-brown);
    border: 6px solid var(--white);
    display: flex; flex-direction: column; align-items: center;
    padding-top: 36px;
    color: var(--white);
    font-size: 29px;
    font-weight: 700;
    line-height: 1.25;
    text-decoration: none;
  }
  .devices-showcase {
    position: absolute;
    left: 650px; top: 45px;
    width: 476px; height: 356px;
    border-radius: 14px;
    background: linear-gradient(160deg, var(--device-light) 0%, var(--device-mid) 100%);
  }
</style>
</head>
<body>
  <section class="banner">
    <div class="banner__wood" role="img" aria-label="Dark weathered wooden surface photograph"></div>
    <svg class="banner__red-field" width="1200" height="458" viewBox="0 0 1200 458" aria-hidden="true">
      <path d="M598 0 Q470 190 472 458 L1200 458 L1200 0 Z" fill="var(--brand-red)"/>
    </svg>

    <h1 class="headline">We have dozens of <strong>Tessary services...</strong></h1>

    <div class="service service--programming"><span>TSX<br>Programing</span></div>
    <div class="service service--finance"><span>Finance</span></div>
    <div class="service service--charts"><span>Charts</span></div>
    <div class="service service--analysis"><span>Data<br>Analysis</span></div>

    <p class="more-note">and many more...</p>

    <a class="purchase-button" href="#"><span>Purchase</span><span>Lumora</span></a>

    <div class="devices-showcase" role="img" aria-label="Desktop monitor, tablet and phone showing colourful spreadsheet planners and charts"></div>
  </section>
</body>
</html>
```